Painting and decorating services

A flyer that promotes my services as a high quality painter and decorator. My services are fully flexible and we cater for range of customers from the decoration of small homes through to larger businesses. We have the flexibility to work through the night which suits businesses that cannot afford to shut throughout the day. We guarantee a top quality finish and are proud to promote a loyalty scheme for successful referrals.

We are truly a family business that is proud and confident to offer one of the most reliable and friendly services on offer.

Target Market(s)

Family homes, businesses who want offer of 24/7 services

Industry/Entity Type

Painting

Font styles to use
Serif
Sans Serif

Requirements
Must have
• Promotion of reliability, value, quality, service
• Days rates and price work considered
• Promotion of night work
• Loyalty scheme / incentives offerred for referrals
• Concept that we are an extremely hard working team who work extended hours and offer flexibility to customers
• Some picture examples of high quality paint jobs as examples of my work.
• Contact details. Phone 01593847261 or mobile 0763918427 email: tkbrushandrollerworks@quillmail.example
Nice to have
• Notion of friendliness coming across from the advert.
• Commitment to giving the customer what they want and delivering to the highest specifications requested
Should not have
• Any over exaggerated false promises that would make the reader of the flyer believe it's just another blagging tradesman with false marketing and empty promises.

```html
<!DOCTYPE html>
<html lang="en">
<head>
<meta charset="utf-8">
<title>TK Brush and Roller Works – Painting and Decorating</title>
<link rel="stylesheet" href="https://fonts.googleapis.com/css2?family=Bebas+Neue&family=Roboto+Slab:wght@400&family=Signika:wght@400;600&family=Rajdhani:wght@700&display=swap">
<style>
  :root {
    --red: #d8202a;
    --navy: #14294d;
    --blue: #1d4f8c;
    --paper: #f1f1ef;
    --wall: #2c3b55;
    --ink: #1b1b1b;
  }
  * { box-sizing: border-box; margin: 0; padding: 0; }
  html, body { width: 848px; height: 1200px; overflow: hidden; background: #fff; }
  .flyer {
    position: relative; width: 848px; height: 1200px; overflow: hidden;
    background: linear-gradient(180deg, #efefec 0%, #e9e9e7 60%, #f3f3f3 100%);
    font-family: "Signika", sans-serif;
  }
  .hero-photo { position: absolute; left: 0; top: 0; width: 848px; height: 820px; }
  .brand {
    position: absolute; left: 30px; top: 52px;
    display: flex; align-items: center; gap: 12px;
  }
  .brand-square { width: 56px; height: 56px; background: var(--red); }
  .brand-name {
    font-family: "Roboto Slab", serif; font-weight: 400; color: var(--navy);
    font-size: 24px; line-height: 1.1; text-transform: uppercase;
  }
  .headline {
    position: absolute; left: 30px; top: 166px;
    font-family: "Bebas Neue", sans-serif; font-size: 68px; line-height: 64px;
    letter-spacing: 0.5px;
  }
  .headline .accent { color: var(--red); display: block; }
  .headline .base { color: var(--navy); display: block; }
  .intro {
    position: absolute; left: 19px; top: 860px; width: 820px;
    color: var(--blue); font-size: 29.5px; line-height: 39px; font-weight: 400;
  }
  .services {
    position: absolute; left: 20px; top: 972px; width: 816px; list-style: none;
  }
  .service {
    position: absolute; height: 35px; border: 1.5px solid var(--red); border-radius: 18px;
    display: flex; align-items: center; padding-left: 26px;
    font-size: 18.5px; color: var(--ink); background: rgba(255,255,255,0.35);
  }
  .service svg { position: absolute; left: -4px; top: 6px; width: 22px; height: 22px; }
  .contact-bar { position: absolute; left: 0; top: 1148px; width: 848px; height: 52px; }
  .contact-bar .email-band {
    position: absolute; left: 0; top: 0; width: 470px; height: 52px; background: var(--navy);
    clip-path: polygon(0 0, 440px 0, 470px 52px, 0 52px);
  }
  .contact-bar .phone-band {
    position: absolute; left: 448px; top: 0; width: 400px; height: 52px; background: var(--red);
    clip-path: polygon(0 0, 400px 0, 400px 52px, 30px 52px);
  }
  .contact-item {
    position: absolute; top: 0; height: 52px; display: flex; align-items: center; gap: 8px;
    color: #fff; font-family: "Rajdhani", sans-serif; font-weight: 700;
  }
  .contact-email { left: 20px; font-size: 19px; }
  .contact-phone { right: 18px; font-size: 24px; letter-spacing: 0.5px; }
</style>
</head>
<body>
<main class="flyer">
  <svg class="hero-photo" viewBox="0 0 848 820" role="img" aria-label="Photo: decorator in blue overalls carrying a paint bucket beside a paint roller on a freshly painted dark blue wall">
    <defs>
      <linearGradient id="wallTone" x1="0" y1="0" x2="1" y2="1">
        <stop offset="0" stop-color="#3a4a66"/>
        <stop offset="0.6" stop-color="#2a3854"/>
        <stop offset="1" stop-color="#22324f"/>
      </linearGradient>
      <linearGradient id="overallTone" x1="0" y1="0" x2="0" y2="1">
        <stop offset="0" stop-color="#d9d2c2"/>
        <stop offset="0.3" stop-color="#3d68a8"/>
        <stop offset="1" stop-color="#2c5592"/>
      </linearGradient>
    </defs>
    <path d="M470 60 L640 0 L848 0 L848 790 L700 800 L560 760 L420 800 L300 770 L150 745 L0 730 L0 400 L120 420 L340 560 L400 380 L370 260 Z" fill="url(#wallTone)"/>
    <path d="M640 0 L848 0 L848 790 L650 780 L645 420 L620 180 Z" fill="url(#overallTone)"/>
    <rect x="398" y="588" width="190" height="170" rx="6" fill="#e94040" opacity="0.9"/>
  </svg>

  <header class="brand">
    <span class="brand-square"></span>
    <span class="brand-name">TK Brush and<br>Roller Works</span>
  </header>

  <h1 class="headline">
    <span class="accent">Guaranteed</span>
    <span class="accent">Reliability,</span>
    <span class="base">Quality and</span>
    <span class="base">Value Service</span>
  </h1>

  <p class="intro">We are truly a caring business that is proud and confident to provide one of the most reliable and friendly services on offer.</p>

  <ul class="services">
    <li class="service" style="left:0;top:0;width:372px;"><svg viewBox="0 0 22 22"><circle cx="11" cy="11" r="10" fill="#d8202a"/><path d="M6 11h8M11 7l4 4-4 4" stroke="#fff" stroke-width="2.4" fill="none" stroke-linecap="round" stroke-linejoin="round"/></svg>Days rates and price work considered</li>
    <li class="service" style="left:384px;top:0;width:432px;"><svg viewBox="0 0 22 22"><circle cx="11" cy="11" r="10" fill="#d8202a"/><path d="M6 11h8M11 7l4 4-4 4" stroke="#fff" stroke-width="2.4" fill="none" stroke-linecap="round" stroke-linejoin="round"/></svg>Loyalty scheme / incentives offerred for referrals</li>
    <li class="service" style="left:0;top:48px;width:382px;"><svg viewBox="0 0 22 22"><circle cx="11" cy="11" r="10" fill="#d8202a"/><path d="M6 11h8M11 7l4 4-4 4" stroke="#fff" stroke-width="2.4" fill="none" stroke-linecap="round" stroke-linejoin="round"/></svg>Painters that will treat your job with respect</li>
    <li class="service" style="left:400px;top:48px;width:416px;"><svg viewBox="0 0 22 22"><circle cx="11" cy="11" r="10" fill="#d8202a"/><path d="M6 11h8M11 7l4 4-4 4" stroke="#fff" stroke-width="2.4" fill="none" stroke-linecap="round" stroke-linejoin="round"/></svg>Flexibility to carry out night work if required</li>
    <li class="service" style="left:0;top:96px;width:408px;"><svg viewBox="0 0 22 22"><circle cx="11" cy="11" r="10" fill="#d8202a"/><path d="M6 11h8M11 7l4 4-4 4" stroke="#fff" stroke-width="2.4" fill="none" stroke-linecap="round" stroke-linejoin="round"/></svg>Hard working team who work extended hours</li>
    <li class="service" style="left:418px;top:96px;width:398px;"><svg viewBox="0 0 22 22"><circle cx="11" cy="11" r="10" fill="#d8202a"/><path d="M6 11h8M11 7l4 4-4 4" stroke="#fff" stroke-width="2.4" fill="none" stroke-linecap="round" stroke-linejoin="round"/></svg>Highly flexible service</li>
  </ul>

  <footer class="contact-bar">
    <div class="email-band"></div>
    <div class="phone-band"></div>
    <div class="contact-item contact-email">
      <svg width="20" height="15" viewBox="0 0 20 15"><rect x="1" y="1" width="18" height="13" fill="none" stroke="#fff" stroke-width="1.4"/><path d="M1 1l9 7 9-7M1 14l6-6M19 14l-6-6" fill="none" stroke="#fff" stroke-width="1.4"/></svg>
      tkbrushandrollerworks@quillmail.example
    </div>
    <div class="contact-item contact-phone">
      <svg width="20" height="20" viewBox="0 0 24 24"><path d="M6.6 10.8a15 15 0 006.6 6.6l2.2-2.2a1 1 0 011-.25 11.4 11.4 0 003.6.57 1 1 0 011 1V20a1 1 0 01-1 1A17 17 0 013 4a1 1 0 011-1h3.5a1 1 0 011 1c0 1.25.2 2.45.57 3.6a1 1 0 01-.25 1z" fill="none" stroke="#fff" stroke-width="1.6"/></svg>
      01593847261 / 0763918427
    </div>
  </footer>
</main>
</body>
</html>
```